Squarespace website build: Quill literary annual (initial design work supplied)

Our brand guidelines provide the look and feel for the website - we just need someone to create it based on our mock ups!
PLEASE NOTE:
- Please base our website off the website pages within the brief (ie homepage is GREEN)
- please ensure each page will be standalone (not a scrolling home page)
- please only use filtered duotone style photography as a hold, if you think the page needs a photo.
-please not the websites i have provided as an influence - especially BRINE ANNUAL. We want very little photography.

Quill is a literary and arts journal that provides a platform for both emerging and established writers and artists from New Zealand and beyond. We are passionate about sharing insights into the intimate and unique worlds of creatives with short stories, poetry, and art – showcasing raw and unfiltered glimpses into their world.

We have our brand guidelines and logo finalised, with a 'look and feel' design for the website within our attached brand guidelines document. We just need someone to design this simple website on Squarespace for us. It will have five pages and will need a newsletter sign up link:
Home page
About us page
Submissions page
Purchase page
Contact page

DRAFT WEB COPY

ABOUT
QUILL is an independent literary annual journal established in 2022 by Harriet Calloway and Mereana Platt that publishes unrepentant unfiltered accounts of life, eclectic takes on the mundane ordinary, and deep dives into modern love & sexuality.
Founder, Editor: Harriet Anahera Calloway
Founder, Production Director: Mereana Platt
Art Direction: Corin Ashby
Editorial Assistant: Lucy Fenwick-Dorsey

I suggest duotone fashion-esque photography which is very Marla Quiggin/ Palm Springs vibe but not obviously identifiable.
· I love the style of Rex Havelin for our shoot in particular. Group lazing around a pool, leisurely, glam, but effortless and ironically looking very natural – as though – yes, these are our lives.
SUBMISSION PAGE
Quill welcomes submissions all year round.
We are drawn to dark humour, satirical takes on the social scene, and starkly honest accounts of ordinary life. Diversity is celebrated, adversity is welcomed and, above all, personal expression is championed. We are particularly seeking content that takes risks, screams of honesty and celebrates life’s most extraordinary moments.
Selected works will be published in our annual publication.

Submission guidelines
We accept flash fiction, short stories and poetry. Individual entries not to mustn’t exceed 2000 words.
Submitted work must be unpublished and in English. We welcome simultaneous submissions, but must be notified immediately if your manuscript is accepted for publication elsewhere or appears in any print or online source. We will endeavour to respond to all submissions within four weeks.
Please send submissions as a word document along with a brief bio of 50 words to inkwell@quilljournal.example
PO Box[EB2]
​Note on Copyright: Copyright remains with the author.

Annual short story competition
Issue One is interested in all that is spiritual, coincidental, or mysterious. Stories selected for this issue reflect life’s uncanny moments, those that defy explanation, and experiences that promote personal and spiritual growth. Entires must be no longer than 2000 words.

First prize: 1000
Second prize: 500
Third prize: 200[EB3]

SUPPORT US
Since our launch in 2022, we have relied upon the generous support of our creative business community in Wellington City, New Zealand. If you read us, or love our ethos, please consider a donation.
Link to chipinhere page
Updates

Hello designers
I would ideally love to have someone turn this around within a few weeks, because the design work has mostly been provided.
Thanks
Harriet

Hi everyone Please ensure you read our brand guidelines and follow the brief. Please note we do not yet have a product, as this is a new venture, so there is no point including images of a magazine that doesn't yet exist. Some further comment to ensure we get there: - We want all pages to be separate pages (not a scrolling home page) with a different colour based on the guidelines - The home page must look just as it does in the brand guidelines - There is no archive page (please read brief) as we have no archive yet. The pages are: Home, About, Contact, Competitions and submissions Thank you

Target Market(s)

writers and creatives

Industry/Entity Type

Writing/ creative/ publishing

Coding

Coded - Design and coding required

Number of Pages Required

4 page

Font styles to use
Other font styles liked:
• COTTA and Univers - as per brand guidelines

Requirements
Must have
• Squarespace designer needed to design our mocked up webpages.
Nice to have
• As close to the brand guideline mock ups as possible (see page 11,12,13)
Should not have
• anything outside of the brand guidelines

```html
<!DOCTYPE html>
<html lang="en">
<head>
<meta charset="utf-8">
<title>Quill — Literary Annual</title>
<link rel="stylesheet" href="https://fonts.googleapis.com/css2?family=Gloock&family=Libre+Caslon+Text:wght@400;700&family=Oswald:wght@300&display=swap">
<style>
:root{
  --plum:#6e2f5e;
  --rose:#b03a5b;
  --rose-soft:#bd5a78;
  --blush:#f2d6de;
  --cream:#efe8dc;
  --paper:#f0ebe0;
  --olive:#5f7432;
  --olive-deep:#6b7a2e;
  --gold:#c7a914;
  --yellow:#e8c43a;
  --ink:#222;
  --white:#fff;
}
*{box-sizing:border-box;margin:0;padding:0}
html,body{width:1200px;height:3525px;overflow:hidden}
body{position:relative;background:var(--white);font-family:"Libre Caslon Text",Georgia,serif;color:var(--ink)}

/* header + hero */
.hero{position:absolute;left:0;top:0;width:1200px;height:718px;background:var(--cream)}
.brand{position:absolute;left:82px;top:14px;font-family:"Gloock",serif;font-size:74px;color:var(--plum);line-height:1}
.nav{position:absolute;left:391px;top:42px;display:flex;gap:26px;font-size:19px;color:var(--ink);white-space:nowrap}
.social{position:absolute;left:930px;top:46px;display:flex;gap:10px;font-size:12px;color:var(--ink);white-space:nowrap}
.cart{position:absolute;left:1142px;top:42px}
.hero-photo{position:absolute;left:101px;top:162px;width:467px;height:493px;background:linear-gradient(150deg,#9a4a66,#6e2a45);box-shadow:0 6px 14px rgba(0,0,0,.3)}
.hero-frame{position:absolute;left:18px;top:18px;right:18px;bottom:16px;border:2px solid var(--white)}
.welcome{position:absolute;left:616px;top:252px;font-size:33px;letter-spacing:.5px}
.hero-title{position:absolute;left:612px;top:290px;font-family:"Gloock",serif;font-size:120px;font-weight:400;color:var(--plum);line-height:1.05}
.hero-lede{position:absolute;left:617px;top:452px;width:480px;font-size:30px;line-height:1.37}

/* magazine */
.mag-title{position:absolute;left:0;width:1200px;top:793px;text-align:center;font-size:30px;font-weight:400;color:var(--rose)}
.mag-intro{position:absolute;left:0;width:1200px;top:842px;text-align:center;font-size:16.5px;line-height:1.55}
.cover{position:absolute;overflow:hidden}
.cover-head{position:absolute;left:0;right:0;top:20px;display:flex;align-items:center;justify-content:space-between;padding:0 18px}
.cover-label{font-family:"Oswald",sans-serif;font-weight:300;font-size:13px}
.cover-name{font-family:"Gloock",serif;font-size:64px;line-height:1}
.cover-frame{position:absolute;left:14px;right:14px;top:140px;bottom:-2px;border:1px solid currentColor}
.cover-photo{position:absolute;left:26px;right:26px;top:152px;bottom:0}
.card-text{position:absolute;white-space:nowrap}
.card-date{font-size:17px}
.card-title{font-weight:700;font-size:29px;color:var(--rose);margin-top:12px}
.card-desc{font-size:21px;margin-top:6px}
.card-link{display:inline-block;margin-top:12px;font-size:17px;color:var(--rose);text-decoration:underline}

/* about */
.about{position:absolute;left:0;top:2128px;width:1200px;height:1397px;background:var(--olive)}
.about-art{position:absolute;left:76px;top:64px;width:467px;height:492px;overflow:hidden;background:linear-gradient(160deg,#d49ab6,#b98fb8)}
.about-wordmark{position:absolute;left:0;right:0;top:160px;text-align:center;font-family:"Gloock",serif;font-size:150px;line-height:1;color:var(--white)}
.about-body{position:absolute;left:612px;top:95px;width:540px;color:var(--white)}
.about-body h2{font-weight:400;font-size:38px}
.about-body p{width:510px;font-size:14.5px;font-weight:700;line-height:1.72;margin-top:20px}
.roles{margin-top:28px;font-size:22px;font-weight:700;line-height:1.85;white-space:nowrap}
.roles span{color:var(--yellow)}
.btn-learn{display:inline-block;margin-top:28px;width:212px;height:64px;line-height:64px;text-align:center;background:var(--cream);color:var(--ink);font-size:25px}

/* newsletter */
.signup{position:absolute;left:75px;top:642px;width:1045px;height:560px;background:radial-gradient(ellipse at 50% 45%,#c5a85e,#a88a40 60%,#7d5c18)}
.signup h3{position:absolute;left:0;right:0;top:220px;text-align:center;font-weight:400;font-size:31px;color:var(--white)}
.signup p{position:absolute;left:0;right:0;top:268px;text-align:center;font-size:14.5px;color:var(--white)}
.field{position:absolute;left:329px;top:312px;width:240px;height:56px;background:var(--white);font-size:13px;padding:20px 14px;color:#333;white-space:nowrap;overflow:hidden}
.btn-sign{position:absolute;left:590px;top:312px;width:119px;height:56px;background:var(--olive);color:var(--white);font-size:22px;font-weight:700;text-align:center;line-height:56px}
.foot-social{position:absolute;left:0;right:0;top:1265px;display:flex;justify-content:center;gap:22px;color:var(--white);font-size:15px}
.copyright{position:absolute;left:0;right:0;top:1335px;text-align:center;color:var(--white);font-size:16px}
</style>
</head>
<body>

<header class="hero">
  <div class="brand">Quill</div>
  <nav class="nav"><span>Home</span><span>About Us</span><span>Submissions</span><span>Purchase</span><span>Contact</span></nav>
  <div class="social"><span>Chatterly</span><span>Lenscape</span><span>Reelhouse</span></div>
  <svg class="cart" width="24" height="22" viewBox="0 0 24 22" aria-label="Cart"><path d="M1 2h4l3 12h12l3-9H7" fill="none" stroke="#6e2f5e" stroke-width="2.4"/><circle cx="9" cy="19" r="2" fill="#6e2f5e"/><circle cx="19" cy="19" r="2" fill="#6e2f5e"/></svg>
  <div class="hero-photo" role="img" aria-label="Duotone plum portrait photograph"><div class="hero-frame"></div></div>
  <div class="welcome">WELCOME TO</div>
  <h1 class="hero-title">Quill</h1>
  <p class="hero-lede">Quill is a plucky little pubication out of Wellington, New Zealand</p>
</header>

<h2 class="mag-title">MAGAZINE</h2>
<p class="mag-intro">Since our launch in 2022, we have relied upon the generous support of our creative business community<br>in Wellington City, New Zealand.</p>

<div class="cover" style="left:83px;top:921px;width:325px;height:434px;background:var(--olive-deep);color:var(--gold)">
  <div class="cover-head"><span class="cover-label">ISSUE 001</span><span class="cover-name">Quill</span><span class="cover-label">DEC 2022</span></div>
  <div class="cover-frame"></div>
  <div class="cover-photo" role="img" aria-label="Duotone pink portrait photograph" style="background:linear-gradient(160deg,#c0607c,#a34466)"></div>
</div>
<div class="card-text" style="left:83px;top:1367px"><div class="card-date">07/28/22</div><div class="card-title">First prize : $100</div><div class="card-desc">Annual short story competition</div><span class="card-link">Read More</span></div>

<div class="cover" style="left:440px;top:927px;width:322px;height:298px;background:var(--rose-soft);color:var(--blush)">
  <div class="cover-head"><span class="cover-label">ISSUE 001</span><span class="cover-name">Quill</span><span class="cover-label">DEC 2022</span></div>
  <div class="cover-frame"></div>
  <div class="cover-photo" role="img" aria-label="Glowing light painting photograph on dark background" style="background:radial-gradient(circle at 50% 40%,#c06aa0,#5a2448 60%,#3a1a3c)"></div>
</div>
<div class="card-text" style="left:441px;top:1248px"><div class="card-date">07/28/22</div><div class="card-title">Second prize: $ 500</div><div class="card-desc">Annual short story competition</div><span class="card-link">Read More</span></div>

<div class="cover" style="left:796px;top:927px;width:322px;height:427px;background:var(--paper);color:var(--olive-deep)">
  <div class="cover-head"><span class="cover-label">ISSUE 001</span><span class="cover-name">Quill</span><span class="cover-label">DEC 2022</span></div>
  <div class="cover-frame"></div>
  <div class="cover-photo" role="img" aria-label="Duotone yellow photograph of a group outdoors" style="background:linear-gradient(180deg,#dcc45a,#b8a656 70%,#8e8448)"></div>
</div>
<div class="card-text" style="left:796px;top:1367px"><div class="card-date">07/28/22</div><div class="card-title">Third prize:&nbsp; $ 200[EB3]</div><div class="card-desc">Annual short story competition</div><span class="card-link">Read More</span></div>

<div class="cover" style="left:75px;top:1516px;width:322px;height:428px;background:var(--paper);color:var(--rose-soft)">
  <div class="cover-head"><span class="cover-label">ISSUE 001</span><span class="cover-name">Quill</span><span class="cover-label">DEC 2022</span></div>
  <div class="cover-frame" style="color:#b0a060"></div>
  <div class="cover-photo" role="img" aria-label="Photograph of open books by candlelight" style="background:linear-gradient(150deg,#4e4a30,#8a7650 50%,#5a4a34)"></div>
</div>
<div class="card-text" style="left:75px;top:1958px"><div class="card-date">07/28/22</div><div class="card-title">First prize : $100</div><div class="card-desc">Annual short story competition</div><span class="card-link">Read More</span></div>

<div class="cover" style="left:436px;top:1401px;width:322px;height:299px;background:var(--gold);color:var(--olive-deep)">
  <div class="cover-head"><span class="cover-label" style="color:var(--rose-soft)">ISSUE 001</span><span class="cover-name">Quill</span><span class="cover-label" style="color:var(--rose-soft)">DEC 2022</span></div>
  <div class="cover-frame"></div>
  <div class="cover-photo" role="img" aria-label="Duotone green interior photograph" style="background:linear-gradient(160deg,#6b7a2e,#b4a424 60%,#7d8a32)"></div>
</div>
<div class="card-text" style="left:437px;top:1723px"><div class="card-date">07/28/22</div><div class="card-title">Second prize: $ 500</div><div class="card-desc">Annual short story competition</div><span class="card-link">Read More</span></div>

<div class="cover" style="left:796px;top:1516px;width:322px;height:428px;background:var(--rose-soft);color:var(--blush)">
  <div class="cover-head"><span class="cover-label">ISSUE 001</span><span class="cover-name">Quill</span><span class="cover-label">DEC 2022</span></div>
  <div class="cover-frame"></div>
  <div class="cover-photo" role="img" aria-label="Duotone underwater photograph of a diver" style="background:linear-gradient(180deg,#4a5090,#6a5088 60%,#7a5080)"></div>
</div>
<div class="card-text" style="left:796px;top:1958px"><div class="card-date">07/28/22</div><div class="card-title">Third prize:&nbsp; $ 200[EB3]</div><div class="card-desc">Annual short story competition</div><span class="card-link">Read More</span></div>

<section class="about">
  <div class="about-art" role="img" aria-label="Duotone pink photograph of arched corridor with the Quill name"><div class="hero-frame"></div><div class="about-wordmark">Quill</div></div>
  <div class="about-body">
    <h2>ABOUT</h2>
    <p>QUILL is an independent literary annual journal established in 2022 by Harriet Calloway and Mereana Platt that publishes unrepentant unfiltered accounts of life, eclectic takes on the mundane ordinary, and deep dives into modern love &amp; sexuality.</p>
    <div class="roles">
      <div><span>Founder, Editor:</span> Harriet Anahera Calloway</div>
      <div><span>Founder, Production Director:</span> Mereana Platt</div>
      <div><span>Art Direction:</span> Corin Ashby</div>
      <div><span>Editorial Assistant:</span> Lucy Fenwick-Dorsey</div>
    </div>
    <span class="btn-learn">Learn More</span>
  </div>

  <div class="signup" role="img" aria-label="Duotone gold portrait photograph behind newsletter form">
    <h3>Get the low-down.</h3>
    <p>Sign up with your email address to receive news and updates.</p>
    <div class="field">inkwell@quilljournal.example</div>
    <div class="btn-sign">Sign Up</div>
  </div>

  <div class="foot-social"><span>Chatterly</span><span>Lenscape</span><span>Reelhouse</span></div>
  <div class="copyright">© copyrights 2022 Quill |&nbsp; All Rights Reserved</div>
</section>

</body>
</html>
```